Lindenfall Studio Business cards

Design our business cards and eventually a logo. The company is based in Paris, its activity is the retailing via internet of luxury home furniture (like Vantorelli, Bercasso, fradusi...) Our clients are international andwith a high sense of aesthetics. The design shall communicate wealth and trust with a high quality and aesthetic sense, pure lines Company Name is Lindenfall StudioExplanation of the name: usually people who wants to buy furniture usually go in a showroom. Today they go in showroom to test the furniture and they search for the price on internet, which is a "Lindenfall studio".We will not be a e-commerce site. Our site will be (another project) a presentation site which purpose is to reach qualified prospects. Then everything will be handled by phone, meeting etc.The business card must be professional as we will negotiate with many luxury brands, opportunity to represent them on our site, prices etc.As far as the color are concerned mostly black and whithe or grey. The font of the Lindenfall Studio name shall have some impact.

Target Market(s)

High-end furniture and buyers of luxury goods, international customers, mostly women who handle such projects.
We also deal with professional buyers (hotels as an example) and luxury brands

Contact Information for Business Card

standard format 85x55, lanscape card, square corners will be printed on thick high quality paper (300 or 350g)

Font styles to use
Sans Serif

Colors

Designer to choose colors to be used in the design.

Requirements
Must have
• Must be white, as the paper will be high quality, the paper will enhance the card.
• Name of the brand Lindenfall studio (with specific font which make it very nice looking and catch the attention. similar to Calibri or Calibri
• Name of person (will give you the name later (4 names and position)
• the position of the person
• Mobile phone, e-mail, Physical address 27, rue Caldenois, 75005 Paris, France (courrier only) our web site www.lindenfallstudio-example.fr
• The card must be simple and class
Nice to have
• Font of the address is smaller than the rest,
• Calibri font or similar on recto side with the name of the company which may look similar to the picture inserted in the brief.
• The grey color in the picture inserted is ok for us
Should not have
• Any parallel lines which represent the name of the company
• Any heavy design If you go on internet sites which present the furniture all designs are pure lines and high quality craftsmanship. To have an idea of our targetted client or brand we will be in touch: https://www.casavornetta-example.it/projects/
• Note that the picture added below is what we use, now as mail signature, up to you to have a better design etc.

```html
<!DOCTYPE html>
<html lang="en">
<head>
<meta charset="utf-8">
<title>Lindenfall Studio – Business Cards</title>
<link rel="stylesheet" href="https://fonts.googleapis.com/css2?family=Open+Sans:wght@400;600;700&display=swap">
<style>
  :root {
    --backdrop: #e4d5c5;
    --paper: #e5e3e2;
    --ink: #474747;
    --ink-soft: #555555;
  }
  * { margin: 0; padding: 0; box-sizing: border-box; }
  html, body {
    width: 742px;
    height: 1200px;
    overflow: hidden;
    background: var(--backdrop);
    font-family: "Open Sans", Calibri, Arial, sans-serif;
  }
  .canvas {
    position: relative;
    width: 742px;
    height: 1200px;
  }
  .card {
    position: absolute;
    left: 93px;
    width: 561px;
    height: 368px;
    background: var(--paper);
    color: var(--ink);
  }
  .card--front { top: 154px; }
  .card--back  { top: 680px; }

  .holder {
    position: absolute;
    left: 38px;
    top: 192px;
  }
  .holder__name {
    font-size: 25px;
    font-weight: 700;
    letter-spacing: 0.2px;
    line-height: 1;
  }
  .holder__role {
    margin-top: 8px;
    font-size: 13.5px;
    font-weight: 600;
    color: var(--ink-soft);
    line-height: 1;
  }

  .contact {
    position: absolute;
    left: 378px;
    top: 162px;
    font-size: 12.5px;
    font-weight: 600;
    line-height: 20px;
    color: var(--ink-soft);
  }
  .contact__address {
    margin-top: 41px;
    font-size: 12px;
    font-weight: 400;
  }

  .brand {
    position: absolute;
    left: 0;
    right: 0;
    top: 164px;
    text-align: center;
    font-size: 36px;
    font-weight: 700;
    line-height: 1;
    white-space: nowrap;
  }
</style>
</head>
<body>
  <main class="canvas">
    <section class="card card--front" aria-label="Card front">
      <div class="holder">
        <p class="holder__name">MAËL DOUCERIN</p>
        <p class="holder__role">PRESEIDENT &amp; CO-FOUNDER</p>
      </div>
      <div class="contact">
        <p>+33612480937</p>
        <p>info@lindenfallstudio-example.fr</p>
        <p>www.lindenfallstudio-example.fr</p>
        <div class="contact__address">
          <p>27, rue Caldenois</p>
          <p>75005 Paris, France</p>
        </div>
      </div>
    </section>

    <section class="card card--back" aria-label="Card back">
      <p class="brand">LINDENFALL STUDIO SAS</p>
    </section>
  </main>
</body>
</html>
```